Heritage Hollow Business Cards

Require a business card design. <br/><br/>Needs to include logo (either round or long version) plus these details:<br/>Maya Torvel<br/>Heritage Hollow<br/>maya@quonbrook.com.au<br/>02 6481 7390<br/>PO Box Glenwarra NSW 2913<br/>www.heritagehollow.com.au<br/><br/>I need in an editable format so that I can create for multiple staff members. <br/><br/>

Target Market(s)

We are an online store selling renovation products to home owners are builders. Looking for a classic classy design.

Industry/Entity Type

Home And Garden

Contact Information for Business Card

Maya Torvel
Heritage Hollow
maya@quonbrook.com.au
02 6481 7390
PO Box Glenwarra NSW 2913
www.heritagehollow.com.au

Colors

Designer to choose colors to be used in the design.

Requirements
Must have
• Must include Logo.

```html
<!DOCTYPE html>
<html lang="en">
<head>
<meta charset="utf-8">
<title>Heritage Hollow Business Cards</title>
<link rel="stylesheet" href="https://fonts.googleapis.com/css2?family=Montserrat:wght@400;600;800&display=swap">
<style>
  :root {
    --page-bg: #d6d6d6;
    --card-bg: #1d1b1c;
    --frame-line: #8e8e8e;
    --text-main: #ffffff;
    --text-soft: #e2e2e2;
    --divider: #bdbdbd;
  }
  * { box-sizing: border-box; margin: 0; padding: 0; }
  html, body {
    width: 1200px;
    height: 800px;
    overflow: hidden;
  }
  body {
    background: var(--page-bg);
    font-family: "Montserrat", sans-serif;
    display: flex;
    align-items: center;
    justify-content: center;
    gap: 40px;
  }
  .card {
    position: relative;
    width: 540px;
    height: 309px;
    background: var(--card-bg);
    border-radius: 22px;
    color: var(--text-main);
    overflow: hidden;
  }
  .card__frame {
    position: absolute;
    inset: 14px;
    border: 1.5px solid var(--frame-line);
    border-radius: 14px;
  }
  /* Info side */
  .card--info .identity {
    position: absolute;
    left: 48px;
    top: 126px;
  }
  .identity__name {
    font-weight: 800;
    font-size: 27px;
    letter-spacing: 1.5px;
    text-transform: uppercase;
    line-height: 1;
  }
  .identity__web {
    margin-top: 9px;
    font-weight: 600;
    font-size: 11.5px;
    letter-spacing: 0.3px;
    color: var(--text-soft);
  }
  .card--info .divider {
    position: absolute;
    left: 292px;
    top: 94px;
    width: 1px;
    height: 118px;
    background: var(--divider);
  }
  .contact {
    position: absolute;
    left: 312px;
    top: 96px;
    font-size: 12px;
    line-height: 1.45;
    color: var(--text-soft);
  }
  .contact__company {
    font-weight: 600;
    color: var(--text-main);
  }
  .contact__row {
    display: flex;
    align-items: center;
    gap: 7px;
  }
  .contact__rows { margin-top: 6px; }
  .contact__icon { width: 10px; height: 10px; fill: var(--text-main); flex: none; }
  /* Brand side */
  .card--brand .brand {
    position: absolute;
    inset: 0;
    display: flex;
    align-items: center;
    justify-content: center;
    gap: 16px;
  }
  .brand__dot {
    width: 44px;
    height: 44px;
    border: 2px solid var(--text-main);
    border-radius: 50%;
  }
  .brand__name {
    font-weight: 400;
    font-size: 38px;
    letter-spacing: 0.5px;
    color: var(--text-main);
  }
</style>
</head>
<body>
  <section class="card card--info">
    <div class="card__frame"></div>
    <div class="identity">
      <p class="identity__name">Maya Torvel</p>
      <p class="identity__web">www.heritagehollow.com.au</p>
    </div>
    <div class="divider"></div>
    <div class="contact">
      <p class="contact__company">Heritage Hollow</p>
      <p>PO Box Glenwarra</p>
      <p>NSW 2913</p>
      <div class="contact__rows">
        <p class="contact__row">
          <svg class="contact__icon" viewBox="0 0 24 24" aria-hidden="true"><path d="M6.6 10.8c1.4 2.8 3.8 5.1 6.6 6.6l2.2-2.2c.3-.3.7-.4 1-.2 1.1.4 2.3.6 3.6.6.6 0 1 .4 1 1V20c0 .6-.4 1-1 1C10.6 21 3 13.4 3 4c0-.6.4-1 1-1h3.5c.6 0 1 .4 1 1 0 1.3.2 2.5.6 3.6.1.3 0 .7-.2 1l-2.3 2.2z"/></svg>
          <span>02 6481 7390</span>
        </p>
        <p class="contact__row">
          <svg class="contact__icon" viewBox="0 0 24 24" aria-hidden="true"><path d="M2 5h20v14H2z M2 5l10 8 10-8" fill="none" stroke="#fff" stroke-width="2.4"/></svg>
          <span>maya@quonbrook.com.au</span>
        </p>
      </div>
    </div>
  </section>

  <section class="card card--brand">
    <div class="card__frame"></div>
    <div class="brand">
      <span class="brand__dot"></span>
      <span class="brand__name">Heritage Hollow</span>
    </div>
  </section>
</body>
</html>
```